Meadow Reset sale graphics for social media

You MUST read the Brief in the WORD document and follow the instructions there. I want to create 10 social media graphics (new Instagram size 4:5 (1080 x 1350 pixels) focusing on our Mother’s Day Meadow Reset Sale graphics, using any of the pics attached. Use the attached pics, NO RANDOM STOCK PHOTOGRAPHY. For the color scheme of the graphics, they should all be complementary to the product colors or feel like Spring time.

Target Market(s)

primarily women

Requirements
Must have
• the photos and text attached

```html
<!DOCTYPE html>
<html lang="en">
<head>
<meta charset="utf-8">
<title>Meadow Reset – Mother's Day Sale Graphics</title>
<link rel="stylesheet" href="https://fonts.googleapis.com/css2?family=Bebas+Neue&family=Anton&family=Oswald:wght@300;500&family=Roboto+Condensed:wght@700;900&display=swap">
<style>
  :root {
    --board: #2a1a2a;
    --plum: #7e4b7f;
    --plum-text: #7a4a7c;
    --red: #f3282b;
    --sun: #fbbd1a;
    --forest: #24503f;
    --sky: #6aa3f0;
    --cobalt: #4f6fd6;
    --ink: #231f20;
    --paper: #ffffff;
    --mist: #ededed;
  }
  * { margin: 0; padding: 0; box-sizing: border-box; }
  html, body { width: 1200px; height: 3119px; overflow: hidden; background: var(--board); }
  .board { position: relative; width: 1200px; height: 3119px; background: var(--board); }
  .tile { position: absolute; width: 460px; height: 575px; overflow: hidden; }
  .col-a { left: 127px; } .col-b { left: 613px; }
  .row-1 { top: 81px; } .row-2 { top: 674px; } .row-3 { top: 1269px; } .row-4 { top: 1865px; } .row-5 { top: 2462px; }
  .t { position: absolute; font-family: "Bebas Neue", sans-serif; line-height: 1; white-space: nowrap; }
  .light { font-family: "Oswald", sans-serif; font-weight: 300; text-transform: uppercase; letter-spacing: -1px; }
  .heavy { font-family: "Anton", sans-serif; }
  .rc { font-family: "Roboto Condensed", sans-serif; font-weight: 700; }
  .center { left: 0; right: 0; text-align: center; }
  .band { position: absolute; display: flex; align-items: center; justify-content: center; }
  .photo-scene { position: absolute; inset: 0;
    background: linear-gradient(90deg, var(--plum) 0%, #87557a 30%, #9a7466 58%, #6f4a36 100%); }
  .photo-scene.flip { background: linear-gradient(270deg, var(--plum) 0%, #87557a 35%, #9a7466 62%, #6f4a36 100%); }
  .photo-products { position: absolute; background: linear-gradient(180deg, #f2f2f2 0%, #e2e2e4 60%, #d6d6d8 100%); }
  .photo-faint { position: absolute; inset: 0; background: radial-gradient(ellipse at 60% 70%, #8d5e8d 0%, var(--plum) 60%); }
  .vertical { position: absolute; writing-mode: vertical-rl; transform: rotate(180deg); font-family: "Bebas Neue", sans-serif; line-height: 1; white-space: nowrap; }
</style>
</head>
<body>
<main class="board">

  <!-- 1 -->
  <section class="tile col-a row-1" style="background:var(--mist)">
    <div class="photo-products" style="left:0;top:235px;width:460px;height:250px" role="img" aria-label="Row of four supplement bottles on a white table"></div>
    <div class="t center" style="top:28px;font-size:92px;color:var(--plum-text)">MOTHER'S DAY</div>
    <div class="band" style="left:33px;top:115px;width:396px;height:99px;background:var(--red)">
      <span class="t" style="position:static;font-size:64px;color:var(--paper)">MEADOW RESET SALE</span>
    </div>
    <div class="band" style="left:73px;top:496px;width:316px;height:50px;background:var(--forest)">
      <span class="t" style="position:static;font-size:40px;color:var(--paper)">25% OFF EVERYTHING!</span>
    </div>
  </section>

  <!-- 2 -->
  <section class="tile col-b row-1">
    <div class="photo-scene" role="img" aria-label="Smiling woman in a white cropped sweater standing in a kitchen behind a row of supplement bottles"></div>
    <div class="t" style="left:32px;top:38px;font-size:96px;color:var(--paper)">25% OFF</div>
    <div class="vertical" style="left:28px;bottom:36px;font-size:86px;color:var(--sky)">MOTHER'S DAY</div>
    <div class="vertical" style="left:106px;bottom:36px;font-size:60px;color:var(--sun)">MEADOW RESET SALE</div>
  </section>

  <!-- 3 -->
  <section class="tile col-a row-2">
    <div class="photo-scene" role="img" aria-label="Smiling woman in a white cropped sweater standing in a kitchen behind a row of supplement bottles"></div>
    <div class="t" style="left:27px;top:28px;font-size:82px;color:var(--paper)">25% OFF</div>
    <div class="t" style="left:27px;top:106px;font-size:42px;color:var(--paper)">ALL SUPPLEMENTS</div>
    <div class="t" style="left:27px;top:144px;font-size:52px;color:var(--paper)">MEADOW RESET</div>
    <div class="vertical" style="left:14px;bottom:46px;font-size:190px;color:var(--sun)">SALE!</div>
  </section>

  <!-- 4 -->
  <section class="tile col-b row-2" style="background:var(--paper)">
    <div class="photo-products" style="left:0;top:224px;width:460px;height:216px" role="img" aria-label="Four supplement bottles lined up on a white table"></div>
    <div class="t center" style="top:24px;font-size:118px;color:var(--plum-text)">25% OFF</div>
    <div class="band" style="left:0;top:126px;width:460px;height:98px;background:var(--red)">
      <span class="t" style="position:static;font-size:68px;color:var(--paper)">MEADOW RESET SALE</span>
    </div>
    <div class="t center" style="top:448px;font-size:46px;color:var(--plum-text)">&mdash; SPRING RESET. &mdash;</div>
    <div class="t center" style="top:493px;font-size:68px;color:var(--ink)">SUMMER READY</div>
  </section>

  <!-- 5 -->
  <section class="tile col-a row-3">
    <div class="photo-faint" role="img" aria-label="Faded photo of a woman with supplement bottles under a purple overlay"></div>
    <div class="t center" style="top:40px;font-size:104px;color:var(--sun)">25% OFF</div>
    <div class="t light center" style="top:130px;font-size:66px;color:var(--paper)">EVERYTHING</div>
    <div class="t center" style="top:215px;font-size:88px;color:var(--paper)">MOTHER'S DAY</div>
    <div class="t light center" style="top:294px;font-size:72px;color:var(--paper)">MEADOW RESET</div>
    <div class="t heavy center" style="top:352px;font-size:150px;color:var(--sun)">SALE</div>
  </section>

  <!-- 6 -->
  <section class="tile col-b row-3">
    <div class="photo-faint" role="img" aria-label="Faded supplement bottles under a purple overlay"></div>
    <div class="t center" style="top:72px;font-size:98px;color:var(--paper)">25% OFF</div>
    <div class="t center" style="top:166px;font-size:84px;color:var(--paper)">MOTHER'S DAY</div>
    <div class="t heavy center" style="top:226px;font-size:150px;color:var(--sun)">SALE</div>
    <div style="position:absolute;left:126px;top:398px;width:208px;height:3px;background:var(--paper)"></div>
    <div class="t center" style="top:436px;font-size:64px;color:var(--paper)">FEEL AMAZING AGAIN!</div>
  </section>

  <!-- 7 -->
  <section class="tile col-a row-4" style="background:var(--paper)">
    <div class="t center" style="top:66px;font-size:152px;color:var(--plum-text)">25% OFF</div>
    <div class="t center" style="top:190px;font-size:92px;color:#000">MOTHER'S DAY</div>
    <div class="t rc center" style="top:262px;font-size:132px;font-weight:900;color:var(--red);letter-spacing:-3px">Sale</div>
    <div class="band" style="left:0;top:397px;width:460px;height:103px;background:var(--forest)">
      <span class="t rc" style="position:static;font-size:58px;color:var(--paper);letter-spacing:-1px">Refresh Your Body</span>
    </div>
  </section>

  <!-- 8 -->
  <section class="tile col-b row-4">
    <div class="photo-scene" role="img" aria-label="Smiling woman in a white cropped sweater standing in a kitchen behind a row of supplement bottles"></div>
    <div class="t" style="left:31px;top:34px;font-size:104px;color:var(--paper)">25% OFF</div>
    <div class="t" style="left:31px;top:134px;font-size:80px;color:var(--paper)">MEADOW</div>
    <div class="t" style="left:31px;top:210px;font-size:80px;color:var(--paper)">RESET</div>
    <div class="band" style="left:0;top:285px;width:165px;height:77px;background:var(--sun);justify-content:flex-end;padding-right:12px">
      <span class="t" style="position:static;font-size:82px;color:var(--ink)">SALE</span>
    </div>
    <div class="t" style="left:33px;top:370px;font-size:46px;line-height:0.92;color:var(--paper)">SPRING<br>CLEANSE.</div>
    <div class="t" style="left:33px;top:456px;font-size:46px;line-height:0.92;color:var(--sun)">SUMMER<br>GLOW</div>
  </section>

  <!-- 9 -->
  <section class="tile col-a row-5">
    <div class="photo-scene flip" role="img" aria-label="Smiling woman in a white cropped sweater standing in a kitchen behind a row of supplement bottles"></div>
    <div class="t" style="right:27px;top:46px;font-size:94px;color:var(--paper)">25% OFF</div>
    <div class="t" style="right:27px;top:136px;font-size:58px;color:var(--paper)">MOTHER'S DAY</div>
    <div class="band" style="left:240px;top:202px;width:220px;height:87px;background:var(--sun);justify-content:flex-end;padding-right:27px">
      <span class="t" style="position:static;font-size:88px;color:var(--ink)">SALE</span>
    </div>
    <div class="t" style="right:27px;top:302px;font-size:64px;color:var(--sun)">DETOX</div>
    <div class="t" style="right:27px;top:360px;font-size:46px;color:var(--paper)">THIS SPRING.</div>
    <div class="t" style="right:27px;top:410px;font-size:64px;color:var(--sun)">SHINE</div>
    <div class="t" style="right:27px;top:472px;font-size:46px;color:var(--paper)">THIS SUMMER</div>
  </section>

  <!-- 10 -->
  <section class="tile col-b row-5" style="background:var(--paper)">
    <div class="band" style="left:36px;top:63px;width:388px;height:103px;background:var(--red)">
      <span class="t" style="position:static;font-size:120px;color:var(--paper);margin-top:10px">25% OFF</span>
    </div>
    <div class="t center" style="top:172px;font-size:90px;color:var(--plum-text)">MOTHER'S DAY</div>
    <div class="t heavy center" style="top:236px;font-size:142px;color:var(--ink)">SALE</div>
    <div class="t center" style="top:390px;font-size:68px;color:var(--forest)">MEADOW RESET FOR</div>
    <div class="t center" style="top:448px;font-size:76px;color:var(--cobalt)">A SUMMER BODY</div>
  </section>

</main>
</body>
</html>
```